Business card design needed

Hi we need a business card design for a new company based on the central coast NSW Australia
We do cakes for all occasions weddings, birthdays, christenings, engagement partys we also do cookie and cater for functions.
we would like to see the colours silver,black and a bright royal blue. (singapore orchid blue)

Industry/Entity Type

Royal

Contact Information for Business Card

Copperleaf Treats
Special occasions cake's and cookies
copperleaf.treats@mailbarrow.com
Rosalie Thwaite
48 Fernhill Street Walbarra
NSW 2274

```html
<!DOCTYPE html>
<html lang="en">
<head>
<meta charset="utf-8">
<title>Copperleaf Treats – Business Card</title>
<link rel="stylesheet" href="https://fonts.googleapis.com/css2?family=Parisienne&family=Crimson+Text&display=swap">
<style>
  :root {
    --page-bg: #f1eee8;
    --card-blue: #2a8ab0;
    --band-blue: #4cc3f0;
    --silver: #c3c3c3;
    --cupcake-blue: #2a86ac;
    --ink-light: #ffffff;
    --ink-dark: #111111;
  }
  html, body {
    margin: 0;
    padding: 0;
    width: 1200px;
    height: 1200px;
    overflow: hidden;
    background: var(--page-bg);
  }
  .canvas {
    position: relative;
    width: 1200px;
    height: 1200px;
  }
  .card {
    position: absolute;
    left: 50px;
    top: 259px;
    width: 1100px;
    height: 682px;
    overflow: hidden;
    background: var(--card-blue);
  }
  .card-shapes {
    position: absolute;
    inset: 0;
  }
  .brand-name {
    position: absolute;
    left: 173px;
    top: 254px;
    width: 500px;
    margin: 0;
    text-align: center;
    font-family: "Parisienne", cursive;
    font-weight: 400;
    font-size: 82px;
    line-height: 86px;
    color: var(--ink-light);
  }
  .brand-name span { display: block; }
  .tagline {
    position: absolute;
    left: 173px;
    top: 487px;
    width: 500px;
    margin: 0;
    text-align: center;
    font-family: "Crimson Text", serif;
    font-size: 29px;
    line-height: 43px;
    color: var(--ink-dark);
  }
  .tagline span { display: block; }
  .contact {
    position: absolute;
    right: 14px;
    top: 562px;
    text-align: right;
    color: var(--ink-dark);
  }
  .contact-name {
    margin: 0;
    font-family: "Parisienne", cursive;
    font-weight: 400;
    font-size: 40px;
    line-height: 44px;
    color: var(--ink-light);
  }
  .contact-line {
    margin: 0;
    font-family: "Crimson Text", serif;
    font-size: 25px;
    line-height: 29px;
  }
</style>
</head>
<body>
<main class="canvas">
  <section class="card" aria-label="Copperleaf Treats business card">
    <svg class="card-shapes" width="1100" height="682" viewBox="0 0 1100 682" aria-hidden="false">
      <rect class="lower-band" x="0" y="552" width="1100" height="130" fill="var(--band-blue)"/>
      <circle class="silver-disc" cx="427" cy="339" r="365" fill="var(--silver)"/>
      <rect class="cupcake-area" x="180" y="29" width="392" height="596" rx="60"
            fill="var(--cupcake-blue)" role="img"
            aria-label="Cupcake silhouette with swirled frosting"/>
    </svg>

    <h1 class="brand-name"><span>Copperleaf</span><span>Treats</span></h1>
    <p class="tagline"><span>Special occasions</span><span>cakes and cookies</span></p>

    <address class="contact" style="font-style:normal">
      <p class="contact-name">Rosalie Thwaite</p>
      <p class="contact-line">copperleaf.treats@mailbarrow.com</p>
      <p class="contact-line">48 Fernhill Street Walbarra NSW 2274</p>
    </address>
  </section>
</main>
</body>
</html>
```